Flyer for a 1 day conference event - with our design elements

We need a two sided A4 flyer created for our 1 day conference, using our corporate design elements.

It is an exclusive event for high profile professional speakers, and it's important for the flyer to be engaging, professional and clean.

We want the prospective attendees to see how much value there is in the day and to feel the event cannot be missed.

I will need to be able to make small edits back and forth with the successful designer in order to get it just-right. (ie: It won't work if I only get access to 2-3 revisions... but don't worry - I don't intend to request an entire re-design)

Target Market(s)

High profile professional speakers

Industry/Entity Type

Event

Requirements
Must have
• Not too much clutter. Some of own design elements
Nice to have
• A large image/photo. Doesnt have to be of a microphone or stage or curtain (traditional speaker things) .. it could be something 'spring' like because it being held in Spring.
Should not have
• too many colours. too many different fonts. too much clutter.

```html
<!DOCTYPE html>
<html lang="en">
<head>
<meta charset="utf-8">
<title>The MSP Unconvention – Flyer</title>
<link rel="stylesheet" href="https://fonts.googleapis.com/css2?family=Arimo:wght@400;700&family=Mulish:wght@300;400;700&family=Parisienne&display=swap">
<style>
  :root {
    --navy: #1d3d78;
    --blue: #2a5fa8;
    --teal: #1693bf;
    --periwinkle: #86a6cf;
    --photo-top: #2566c8;
    --photo-low: #8fc2ee;
    --lime: #9acd1e;
    --slate: #6e8193;
    --ink: #1b2d52;
    --body-grey: #8a8f96;
    --info-bg: #cfe2f3;
    --info-text: #5f7590;
    --info-strong: #2a5fa8;
    --page-bg: #ffffff;
    --canvas-bg: #ffffff;
  }
  * { box-sizing: border-box; margin: 0; padding: 0; }
  html, body { width: 1200px; height: 900px; overflow: hidden; background: var(--canvas-bg); }
  body { position: relative; font-family: "Arimo", Arial, sans-serif; }

  .page {
    position: absolute; top: 38px; height: 802px; background: var(--page-bg);
    box-shadow: 2px 3px 6px rgba(0,0,0,.35); overflow: hidden;
  }
  .page--front { left: 14px; width: 568px; }
  .page--back { left: 608px; width: 566px; }
  .page-label {
    position: absolute; top: 848px; font-family: "Arimo", Arial, sans-serif;
    font-size: 28px; color: #000;
  }
  .page-label--front { left: 278px; }
  .page-label--back { left: 850px; }

  /* Front */
  .hero-photo {
    position: absolute; left: 0; top: 0; width: 568px; height: 465px;
    background: linear-gradient(180deg, var(--photo-top) 0%, var(--photo-low) 100%);
  }
  .hero-bands { position: absolute; left: 0; top: 0; }
  .hero-themes {
    position: absolute; font-family: "Parisienne", cursive; color: #fff;
    font-size: 27px; transform: rotate(-22deg); transform-origin: left center;
    white-space: nowrap; letter-spacing: 1px;
  }
  .hero-themes--one { left: 192px; top: 230px; }
  .hero-themes--two { left: 270px; top: 240px; }
  .hero-themes--three { left: 232px; top: 310px; }
  .front-strap {
    position: absolute; left: 18px; top: 470px; font-family: "Mulish", sans-serif;
    font-weight: 300; font-size: 19.5px; letter-spacing: 1.6px; color: var(--body-grey);
    white-space: nowrap;
  }
  .event-title {
    position: absolute; left: 56px; top: 541px; font-family: "Mulish", sans-serif;
    font-weight: 400; font-size: 28px; color: var(--blue); white-space: nowrap;
  }
  .event-audience {
    position: absolute; left: 20px; top: 580px; font-family: "Mulish", sans-serif; line-height: 1;
    white-space: nowrap;
  }
  .event-audience__lead { display: block; font-weight: 700; font-size: 57px; color: var(--lime); padding-left: 50px; }
  .event-audience__rest { display: block; font-weight: 300; font-size: 57px; color: var(--slate); margin-top: 2px; }

  .org-mark {
    position: absolute; display: flex; align-items: center; gap: 6px;
    font-family: "Arimo", Arial, sans-serif; font-weight: 700; font-size: 12px;
    line-height: 1.1; color: var(--blue); width: 118px;
  }
  .org-mark__square { width: 14px; height: 14px; background: var(--blue); flex: none; }
  .page--front .org-mark { left: 436px; top: 728px; }
  .page--back .org-mark { left: 436px; top: 714px; }

  /* Back */
  .back-bands { position: absolute; left: 0; top: 0; }
  .agenda-intro {
    position: absolute; left: 18px; top: 13px; width: 230px; color: #fff;
    font-family: "Mulish", sans-serif; font-size: 12.5px; line-height: 1.35; opacity: .9;
  }
  .agenda-section { position: absolute; }
  .agenda-section--intimate { left: 19px; top: 140px; width: 256px; }
  .agenda-section--debate { left: 285px; top: 118px; width: 268px; }
  .agenda-section--insight { left: 288px; top: 422px; width: 268px; }
  .section-title { font-family: "Mulish", sans-serif; font-weight: 400; font-size: 24px; color: var(--lime); line-height: 1.1; white-space: nowrap; }
  .section-tagline { font-family: "Mulish", sans-serif; font-weight: 400; font-size: 16.5px; color: var(--blue); margin: 1px 0 14px 13px; white-space: nowrap; }
  .session { margin-bottom: 11px; }
  .session__name { font-weight: 700; font-size: 10px; color: var(--ink); margin-bottom: 2px; }
  .session__detail { font-size: 9.4px; line-height: 1.33; color: var(--body-grey); }
  .session__detail + .session__detail { margin-top: 10px; }
  .session__list { list-style: none; font-size: 9.4px; line-height: 1.33; color: var(--body-grey); padding-left: 8px; }

  .event-details {
    position: absolute; left: 0; top: 580px; width: 274px; height: 222px;
    background: var(--info-bg); border-top-right-radius: 14px; padding: 22px 0 0 29px;
    font-size: 10.5px; line-height: 1.4; color: var(--info-text);
  }
  .event-details p { margin-bottom: 13px; }
  .event-details strong { font-weight: 400; color: var(--info-strong); }
  .contact-line {
    position: absolute; left: 305px; top: 766px; font-weight: 700; font-size: 10px; color: var(--ink);
    white-space: nowrap;
  }
</style>
</head>
<body>

<section class="page page--front" aria-label="Flyer front">
  <div class="hero-photo" role="img" aria-label="Spring photograph: a dandelion releasing its seeds against a blue sky above fresh green grass"></div>
  <svg class="hero-bands" width="568" height="470" viewBox="0 0 568 470" aria-hidden="true">
    <path d="M0 0 H568 V92 Q300 110 0 315 Z" fill="var(--teal)"/>
    <path d="M0 0 H568 V34 Q250 70 0 280 Z" fill="#2f6f9f"/>
    <path d="M0 0 H470 Q250 40 0 190 Z" fill="var(--navy)"/>
    <path d="M140 0 H568 V34 Q400 6 140 0 Z" fill="var(--teal)"/>
    <path d="M568 40 Q470 60 395 100 Q480 90 568 128 Z" fill="var(--periwinkle)"/>
    <path d="M0 190 Q250 40 470 0" fill="none" stroke="#fff" stroke-width="2.5"/>
    <path d="M0 280 Q250 70 568 34" fill="none" stroke="#fff" stroke-width="2.5"/>
    <path d="M0 315 Q300 110 568 92" fill="none" stroke="#fff" stroke-width="3"/>
  </svg>
  <span class="hero-themes hero-themes--one">instantly intimate</span>
  <span class="hero-themes hero-themes--two">debate and dissent</span>
  <span class="hero-themes hero-themes--three">immediate insight</span>

  <p class="front-strap">No stars. No keynotes. No workshops. No tweets.</p>
  <h1 class="event-title">The MSP Unconvention</h1>
  <p class="event-audience">
    <span class="event-audience__lead">for experienced,</span>
    <span class="event-audience__rest">successful speakers</span>
  </p>
  <div class="org-mark"><span class="org-mark__square"></span><span>Guild of Professional Presenters</span></div>
</section>

<section class="page page--back" aria-label="Flyer back">
  <svg class="back-bands" width="566" height="170" viewBox="0 0 566 170" aria-hidden="true">
    <defs>
      <linearGradient id="bandGrad" x1="0" y1="0" x2="1" y2="0">
        <stop offset="0" stop-color="var(--navy)"/>
        <stop offset="1" stop-color="var(--teal)"/>
      </linearGradient>
    </defs>
    <path d="M0 0 H566 V90 Q300 80 0 108 Z" fill="url(#bandGrad)"/>
    <path d="M340 0 H566 V60 Q470 20 340 0 Z" fill="#3f7fbf" opacity=".7"/>
    <path d="M0 96 Q300 66 566 80" fill="none" stroke="#fff" stroke-width="3"/>
    <path d="M0 108 Q300 80 566 90 V104 Q300 96 0 122 Z" fill="#8fc3e6"/>
    <path d="M0 122 Q300 96 566 104 V110 Q300 104 0 130 Z" fill="#e1eff9"/>
  </svg>
  <p class="agenda-intro">The day's agenda will be made up of a couple of exercises from each of the three sections.</p>

  <div class="agenda-section agenda-section--intimate">
    <h2 class="section-title">Instantly Intimate</h2>
    <p class="section-tagline">Let's get straight into it.</p>
    <div class="session"><h3 class="session__name">Why to Say, When to Say, How to Say No</h3><p class="session__detail">What policies and processes do you have – or need – for declining work you don't really want to do?</p></div>
    <div class="session"><h3 class="session__name">How Much and To Who?</h3><p class="session__detail">How do you decide how much charity work to do, for who and on what basis – and how do you manage it?</p></div>
    <div class="session"><h3 class="session__name">Traveling Rituals</h3><p class="session__detail">What habits and rituals do you have when you travel – in the air, on the ground, in your hotel room – and why?</p></div>
    <div class="session"><h3 class="session__name">Step Inside My Office</h3><p class="session__detail">Five speakers give us a five minute super intimate look at how they manage their business. No frills, no glam, just the basic day to day of it.</p></div>
    <div class="session"><h3 class="session__name">Looking After Yourself</h3><p class="session__detail">How do you manage the physical, mental and psycho-spiritual dangers of being a professional speaker? How do you look after yourself?</p></div>
    <div class="session"><h3 class="session__name">Ask and Answer Five Questions</h3><p class="session__detail">Five minutes each with three other people in which you ask and answer five questions (some given to you, some of your own). You can say Pass up to five times.</p></div>
  </div>

  <div class="agenda-section agenda-section--debate">
    <h2 class="section-title">Debate and Dissent</h2>
    <p class="section-tagline">Let's get some friction and sport.</p>
    <div class="session"><h3 class="session__name">Thumbite Debates</h3>
      <p class="session__detail">Three affirmative, three negative, one minute per person – go.</p>
      <p class="session__detail">Topics will be generated on the day and may include:</p>
      <ul class="session__list">
        <li>That motivational speakers were responsible for the GFC.</li>
        <li>That the GPP has lost its way.</li>
        <li>That bureaus are underappreciated.</li>
        <li>That it is too easy to become a MSP.</li>
        <li>That ego has no place in speaking.</li>
      </ul>
    </div>
    <div class="session"><h3 class="session__name">Help Me Hypothetically</h3><p class="session__detail">Anonymous submissions of ethical challenges receive responses and we discuss.</p></div>
    <div class="session"><h3 class="session__name">Telling People What They Don't Want To Hear</h3><p class="session__detail">Three people will each present a difficult truth to a hostile audience while we explore ways of delivering more confronting, provocative or unpopular ideas and how we might better deal with dissent or discomfort in the room.</p></div>
  </div>

  <div class="agenda-section agenda-section--insight">
    <h2 class="section-title">Immediate Insight</h2>
    <p class="section-tagline">Share what you know or see, fast.</p>
    <div class="session"><h3 class="session__name">Blow My Trumpet For Me</h3><p class="session__detail">Get your promotional copy written by three other people. What does it say? What does it tell you? What do you learn?</p></div>
    <div class="session"><h3 class="session__name">Emergency Presentation</h3><p class="session__detail">You are put into small groups – crack teams – to prepare a keynote from various criteria. Ten minutes to prepare. Five minutes to present your outline.</p></div>
    <div class="session"><h3 class="session__name">Instant Unedited Product Review</h3><p class="session__detail">Get a super-efficient, ruthless critique of one of your products.</p></div>
    <div class="session"><h3 class="session__name">Show Me The Future</h3><p class="session__detail">Webinar, video, social media, blogging, microblogging, podcasts and ebooks – what is going on? Which are you doing? Which are you resisting or declining? What's next?</p></div>
  </div>

  <div class="event-details">
    <p>Facilitator <strong>– Daniel Marsh</strong></p>
    <p>Venue <strong>– xxx Melbourne</strong></p>
    <p>November 5 <strong>– 8:30am - 5pm followed by an optional pub dinner</strong></p>
    <p>Book before Sept 30 <strong>– $195</strong></p>
    <p>After Sept 30 <strong>– $195 PLUS $100 donation to a charity chosen by the group on the day</strong></p>
  </div>

  <div class="org-mark"><span class="org-mark__square"></span><span>Guild of Professional Presenters</span></div>
  <p class="contact-line">Contact Daniel to discuss: daniel@marshtalks.com</p>
</section>

<p class="page-label page-label--front">Front</p>
<p class="page-label page-label--back">back</p>

</body>
</html>
```